New Office Poster Designs

Attached you will find 3 poster designs that we found online along with our logos. Please use our logos to reference any type of color or design.
These posters will be hung around our Loan Offices.

INSTRUCTIONS: Please mimic all 3 posters (MINUS THE SMALL WRITING ON THEM THAT IS NOT IN ENGLISH IGNORE THAT)
but use our logos and colors. Also, if you can make them in Spanish as well as English that is a plus. We will also need 1 additional poster with the below wording.

Additional Poster:
Stuck in a Title Loan? Let us pay it off up to $10,000

Target Market(s)

People looking to get a loan and need money

Industry/Entity Type

Loan Industry - Consumer Lending - Fast easy loans

Requirements
Nice to have
• English and Spanish

```html
<!DOCTYPE html>
<html lang="en">
<head>
<meta charset="utf-8">
<title>Title Loan Payoff Posters</title>
<link rel="stylesheet" href="https://fonts.googleapis.com/css2?family=Poppins:wght@400;500;600;700;800&family=Bebas+Neue&family=Oswald:wght@500&display=swap">
<style>
  :root {
    --stage: #b3b3b3;
    --red: #b51d25;
    --red-dark: #7c1117;
    --green: #0f4a2b;
    --green-dark: #0a3a21;
    --white: #ffffff;
    --outline: #c8141c;
  }
  * { margin: 0; padding: 0; box-sizing: border-box; }
  html, body { width: 1200px; height: 823px; overflow: hidden; }
  body { background: var(--stage); position: relative; font-family: "Poppins", sans-serif; color: var(--white); }

  .poster { position: absolute; top: 76px; width: 492px; height: 656px; overflow: hidden; box-shadow: 0 8px 22px rgba(0,0,0,.35); }
  .poster--en { left: 92px; }
  .poster--es { left: 630px; }
  .poster__art { position: absolute; inset: 0; }

  .headline { position: absolute; left: 0; right: 0; text-align: center; line-height: 1; color: var(--white);
    -webkit-text-stroke: 1px var(--outline); text-shadow: 3px 4px 6px rgba(60,0,0,.55); }
  .headline--en { font-family: "Poppins", sans-serif; font-weight: 800; letter-spacing: -1px; }
  .headline--en.line1 { top: 80px; font-size: 49px; }
  .headline--en.line2 { top: 133px; font-size: 55px; }
  .headline--es { font-family: "Bebas Neue", sans-serif; }
  .headline--es.line1 { top: 80px; font-size: 50px; }
  .headline--es.line2 { top: 126px; font-size: 70px; }

  .offer { position: absolute; left: 0; right: 0; text-align: center; font-weight: 700; font-size: 28px; line-height: 1; letter-spacing: .5px; }
  .offer.line1 { top: 270px; }
  .offer.line2 { top: 303px; }
  .amount { position: absolute; left: 0; right: 0; top: 326px; text-align: center; font-weight: 700; font-size: 82px; line-height: 1; letter-spacing: -1px;
    -webkit-text-stroke: 1px var(--outline); text-shadow: 3px 5px 8px rgba(0,0,0,.5); }

  .brand { position: absolute; left: 37px; width: 210px; top: 500px; text-align: center; font-weight: 500; font-size: 26px; line-height: 1; }

  .limited { position: absolute; left: 37px; top: 563px; font-size: 15px; letter-spacing: 2.5px; line-height: 1; }
  .limited strong { font-weight: 700; }
  .limited span { font-weight: 400; }

  .phone { position: absolute; left: 37px; top: 589px; display: flex; align-items: center; gap: 4px; }
  .phone__icon { width: 22px; height: 22px; }
  .phone__number { font-family: "Oswald", sans-serif; font-weight: 500; font-size: 24px; line-height: 1; }

  .disclaimer { position: absolute; left: 246px; top: 450px; width: 212px; font-size: 6.3px; line-height: 1.28; font-weight: 400; }
  .poster--es .disclaimer { top: 458px; width: 220px; }

  .website { position: absolute; left: 246px; top: 600px; right: 0; display: flex; align-items: center; gap: 4px; font-size: 9.5px; letter-spacing: 1.2px; line-height: 1; }
  .website strong { font-weight: 600; }
  .website__rule { flex: 1; height: 1px; background: var(--white); opacity: .85; margin-top: 4px; }
</style>
</head>
<body>

<section class="poster poster--en" lang="en">
  <svg class="poster__art" viewBox="0 0 492 656" width="492" height="656">
    <defs>
      <linearGradient id="redFieldEn" x1="0" y1="0" x2="1" y2="1">
        <stop offset="0" stop-color="#8e141a"/><stop offset=".5" stop-color="#b51d25"/><stop offset="1" stop-color="#a81a21"/>
      </linearGradient>
      <linearGradient id="greenFieldEn" x1="0" y1="0" x2="0" y2="1">
        <stop offset="0" stop-color="#0f4a2b"/><stop offset=".45" stop-color="#14502f"/><stop offset="1" stop-color="#0d4427"/>
      </linearGradient>
    </defs>
    <rect width="492" height="656" fill="url(#redFieldEn)" role="img" aria-label="Faint photo of a toy car, keys and cash on a keyboard, tinted red"/>
    <rect x="28" y="32" width="438" height="400" fill="none" stroke="#ffffff" stroke-width="1"/>
    <path d="M0 317 Q246 108 492 317 L492 656 L0 656 Z" fill="#ffffff"/>
    <path d="M0 326 Q246 124 492 326 L492 656 L0 656 Z" fill="url(#greenFieldEn)" role="img" aria-label="Faint photo of stacked banknotes and coins, tinted green"/>
  </svg>

  <h1 class="headline headline--en line1">STUCK IN A</h1>
  <h1 class="headline headline--en line2">TITLE LOAN?</h1>
  <p class="offer line1">LET US PAY</p>
  <p class="offer line2">IT OFF UP TO</p>
  <p class="amount">$10,000</p>

  <p class="brand">Crestway Loans</p>

  <p class="limited"><strong>LIMITED</strong> <span>OFFER</span></p>
  <div class="phone">
    <svg class="phone__icon" viewBox="0 0 24 24"><circle cx="12" cy="12" r="10.5" fill="none" stroke="#fff" stroke-width="1.6"/><path d="M8.2 6.5l2 2.4-1.2 1.5c.7 1.6 2 2.9 3.6 3.6l1.5-1.2 2.4 2-1.1 1.9c-3.9-.3-7.8-4.2-8.1-8.1z" fill="#fff"/></svg>
    <span class="phone__number">+1 555-014-2739</span>
  </div>

  <p class="disclaimer">This lender is licensed and regulated by the state financial institutions division. To report any unresolved problem or complaint, contact the division by phone or visit its website. Offers shown contain rate quotes no greater than 35.99% APR with lengths from 12 months to 48 months. Personal loan amounts typically range from $500 to $5,000. Your actual rate depends upon loan amount, loan term, credit usage and history, and will be agreed upon between you and the lender. These disclosures are provided for information only and may not be construed as legal advice.</p>

  <div class="website"><span>www.<strong>crestwayloans</strong>.com</span><span class="website__rule"></span></div>
</section>

<section class="poster poster--es" lang="es">
  <svg class="poster__art" viewBox="0 0 492 656" width="492" height="656">
    <defs>
      <linearGradient id="redFieldEs" x1="0" y1="0" x2="1" y2="1">
        <stop offset="0" stop-color="#8e141a"/><stop offset=".5" stop-color="#b51d25"/><stop offset="1" stop-color="#a81a21"/>
      </linearGradient>
      <linearGradient id="greenFieldEs" x1="0" y1="0" x2="0" y2="1">
        <stop offset="0" stop-color="#0f4a2b"/><stop offset=".45" stop-color="#14502f"/><stop offset="1" stop-color="#0d4427"/>
      </linearGradient>
    </defs>
    <rect width="492" height="656" fill="url(#redFieldEs)" role="img" aria-label="Foto tenue de un auto de juguete, llaves y billetes sobre un teclado, en tono rojo"/>
    <rect x="28" y="32" width="438" height="400" fill="none" stroke="#ffffff" stroke-width="1"/>
    <path d="M0 317 Q246 108 492 317 L492 656 L0 656 Z" fill="#ffffff"/>
    <path d="M0 326 Q246 124 492 326 L492 656 L0 656 Z" fill="url(#greenFieldEs)" role="img" aria-label="Foto tenue de billetes y monedas apilados, en tono verde"/>
  </svg>

  <h1 class="headline headline--es line1">ATASCADO EN UN PRÉSTAMO</h1>
  <h1 class="headline headline--es line2">SOBRE EL TÍTULO?</h1>
  <p class="offer line1">PAGUEMOSLO</p>
  <p class="offer line2">HASTA</p>
  <p class="amount">$10,000</p>

  <p class="brand">Crestway Loans</p>

  <p class="limited"><strong>OFERTA</strong> <span>LIMITADA</span></p>
  <div class="phone">
    <svg class="phone__icon" viewBox="0 0 24 24"><circle cx="12" cy="12" r="10.5" fill="none" stroke="#fff" stroke-width="1.6"/><path d="M8.2 6.5l2 2.4-1.2 1.5c.7 1.6 2 2.9 3.6 3.6l1.5-1.2 2.4 2-1.1 1.9c-3.9-.3-7.8-4.2-8.1-8.1z" fill="#fff"/></svg>
    <span class="phone__number">+1 555-014-2739</span>
  </div>

  <p class="disclaimer">Este prestamista está autorizado y regulado por la división estatal de instituciones financieras. Para informar cualquier problema o queja no resuelta, comuníquese con la división por teléfono o visite su sitio web. Las ofertas contienen tasas no superiores al 35.99% APR con plazos de 12 a 48 meses. Los montos de préstamos personales suelen oscilar entre $500 y $5,000. Su tasa real depende del monto, el plazo, el uso del crédito y el historial, y será acordada entre usted y el prestamista. Estas divulgaciones son solo informativas y no constituyen asesoramiento legal.</p>

  <div class="website"><span>www.<strong>crestwayloans</strong>.com</span><span class="website__rule"></span></div>
</section>

</body>
</html>
```